OBW Crestmark Shipping Limited

We need the buissnes card to be very exclusive. As we are all young in our company. We need this to be the gate to make our clients feel deep interest for us.

We are focused in as International Trade advisors, and our products go from Oil Tanker Ships to Rubber balls for dogs.

Our Slogan is Making Global Local.
And our main marketing will be through Internet.

We were stablished in 2009 In Mexico and we also have offices in Hong Kong.
We have representatives in China and Europe.

Target Market(s)

Is every company or Individual that wants to develop an International Project or product development or Logistic service of Goods and people.
Some of our current projects are Ship Brokerage, Mine Brokerage, Real State and Product Pormotional development.

Industry/Entity Type

It Company

Requirements
Must have
• Our Logo and slogan, and make the card accoriding to the logo.
Nice to have
• Our Colors

```html
<!DOCTYPE html>
<html lang="en">
<head>
<meta charset="utf-8">
<title>OBW Crestmark Shipping Limited – Business Card</title>
<link rel="stylesheet" href="https://fonts.googleapis.com/css2?family=Open+Sans:wght@400;600;700&display=swap">
<style>
  :root {
    --bg: #ece8e2;
    --card-white: #ffffff;
    --navy: #283a93;
    --royal: #1f56b8;
    --sky: #1fa6e0;
    --lime: #8cc63f;
    --ink: #4a4a4a;
    --shadow: rgba(0, 0, 0, 0.18);
  }
  * { margin: 0; padding: 0; box-sizing: border-box; }
  html, body {
    width: 1200px; height: 1024px; overflow: hidden;
    background: var(--bg);
    font-family: "Open Sans", Arial, sans-serif;
  }
  .canvas { position: relative; width: 1200px; height: 1024px; }
  .card {
    position: absolute; left: 220px; width: 760px; height: 434px;
    border-radius: 4px; overflow: hidden;
    box-shadow: 0 10px 28px var(--shadow);
  }
  .card--front { top: 52px; background: var(--card-white); }
  .card--back { top: 538px; background: linear-gradient(135deg, var(--royal) 0%, #1b6fcf 55%, var(--sky) 100%); }

  .card__band { position: absolute; left: 0; top: 0; width: 100%; height: 100%; }

  .brand { position: absolute; display: flex; align-items: center; gap: 12px; }
  .brand__dot { border-radius: 50%; background: var(--royal); }
  .brand__name { font-weight: 700; color: var(--lime); letter-spacing: 2px; line-height: 1; }

  .card--front .brand { right: 70px; top: 44px; }
  .card--front .brand__dot { width: 46px; height: 46px; }
  .card--front .brand__name { font-size: 50px; }

  .contact { position: absolute; left: 48px; top: 118px; }
  .contact__name { font-size: 24px; font-weight: 700; color: var(--royal); letter-spacing: 0.5px; }
  .contact__title { font-size: 15px; font-weight: 700; color: var(--lime); margin-top: 2px; }
  .contact__address { margin-top: 18px; font-size: 17px; color: var(--ink); line-height: 1.3; }
  .contact__list { list-style: none; margin-top: 12px; font-size: 16px; color: var(--ink); line-height: 1.35; }
  .contact__list li { display: flex; align-items: center; gap: 10px; }
  .contact__list svg { width: 14px; height: 14px; flex: none; }

  .front-web {
    position: absolute; right: 44px; bottom: 26px;
    font-size: 16px; font-weight: 600; color: #ffffff; letter-spacing: 0.3px;
  }

  .world-map {
    position: absolute; left: 40px; top: 30px; width: 680px; height: 374px;
    border-radius: 50%;
    background: radial-gradient(ellipse at center, rgba(120, 190, 255, 0.22) 0%, rgba(120, 190, 255, 0) 70%);
  }
  .card--back .brand { left: 50%; top: 50%; transform: translate(-50%, -50%); }
  .card--back .brand__dot { width: 60px; height: 60px; background: var(--sky); }
  .card--back .brand__name { font-size: 62px; }
  .back-web {
    position: absolute; left: 40px; bottom: 30px;
    font-size: 16px; font-weight: 600; color: #ffffff; letter-spacing: 0.3px;
  }
</style>
</head>
<body>
<main class="canvas">

  <section class="card card--front" aria-label="Business card front">
    <svg class="card__band" viewBox="0 0 760 434" preserveAspectRatio="none" aria-hidden="true">
      <path d="M0 434 L0 395 C250 385 470 330 760 175 L760 434 Z" fill="var(--sky)"/>
      <path d="M330 434 L330 385 C480 360 620 290 760 190 L760 434 Z" fill="var(--navy)"/>
      <path d="M190 372 C420 350 600 270 760 150" fill="none" stroke="var(--lime)" stroke-width="7"/>
    </svg>

    <div class="brand">
      <span class="brand__dot"></span>
      <span class="brand__name">OBW</span>
    </div>

    <div class="contact">
      <h1 class="contact__name">MATEO VILLANUEVA</h1>
      <p class="contact__title">JOB TITLE</p>
      <p class="contact__address">Your Address Goes Here, City, Zip Code<br>Country Name<br>P.O.BOX 00000</p>
      <ul class="contact__list">
        <li><svg viewBox="0 0 14 14"><path d="M3 1 L5 1 L6 4 L4.5 5.5 C5.5 7.5 6.5 8.5 8.5 9.5 L10 8 L13 9 L13 11 C13 12 12 13 11 13 C5.5 13 1 8.5 1 3 C1 2 2 1 3 1 Z" fill="var(--lime)"/></svg>0000 0000 000</li>
        <li><svg viewBox="0 0 14 14"><rect x="1" y="1" width="12" height="12" fill="var(--lime)"/><rect x="4" y="4" width="6" height="6" fill="#fff"/></svg>0000 0000 000</li>
        <li><svg viewBox="0 0 14 14"><rect x="1.5" y="1.5" width="11" height="11" fill="none" stroke="var(--ink)" stroke-width="1.2"/></svg>0000 0000 000</li>
        <li><svg viewBox="0 0 14 14"><rect x="1" y="3" width="12" height="9" fill="var(--lime)"/><path d="M1 3 L7 8 L13 3" fill="none" stroke="#fff" stroke-width="1.2"/></svg>info@obwcrestmark.com</li>
      </ul>
    </div>

    <p class="front-web">www.obwcrestmark.com</p>
  </section>

  <section class="card card--back" aria-label="Business card back">
    <div class="world-map" role="img" aria-label="Faint world map in light blue tones"></div>
    <div class="brand">
      <span class="brand__dot"></span>
      <span class="brand__name">OBW</span>
    </div>
    <p class="back-web">www.obwcrestmark.com</p>
  </section>

</main>
</body>
</html>
```